Brightwave Business Card

Professional Business Card Design required using the attached contact information.

Contact information can be rearranged as required.

The company is a new start up venture developing solar systems, the branding should be in keeping with that of one of the investors whose website is as follows https://www.quorvex.com/

```html
<!DOCTYPE html>
<html lang="en">
<head>
<meta charset="utf-8">
<title>Brightwave Renewables – Business Card</title>
<link href="https://fonts.googleapis.com/css2?family=Open+Sans:ital,wght@0,400;0,700;1,400&display=swap" rel="stylesheet">
<style>
  :root {
    --backdrop: #2f4049;
    --paper: #ffffff;
    --teal-light: #5cc2a8;
    --teal-mid: #32a085;
    --teal-band: #22977a;
    --teal-deep: #1a5b4a;
    --name-band: #5b5b5d;
    --ink: #151515;
  }
  * { margin: 0; padding: 0; box-sizing: border-box; }
  html, body {
    width: 1200px; height: 900px; overflow: hidden;
    background: var(--backdrop);
    font-family: "Open Sans", Arial, sans-serif;
  }
  .card {
    position: absolute; left: 75px; top: 150px;
    width: 1050px; height: 600px;
    background: var(--paper);
    box-shadow: 0 18px 40px rgba(0,0,0,0.35);
    overflow: hidden;
  }
  .edge-art { position: absolute; top: 0; height: 600px; }
  .edge-art--left { left: 0; width: 280px; }
  .edge-art--right { left: 620px; width: 430px; }
  .brand {
    position: absolute; left: 180px; top: 52px;
    display: flex; align-items: center; gap: 14px;
  }
  .brand-dot {
    width: 14px; height: 14px; border-radius: 50%;
    background: var(--teal-band);
  }
  .brand-name {
    font-weight: 700; font-size: 34px; letter-spacing: 3px;
    color: var(--ink); text-transform: uppercase;
  }
  .contact {
    position: absolute; left: 146px; top: 326px;
    list-style: none; color: var(--ink); font-size: 19px;
  }
  .contact li { display: flex; align-items: flex-start; gap: 26px; margin-bottom: 12px; line-height: 1.35; }
  .contact svg { width: 24px; height: 24px; flex: none; fill: #fff; margin-top: 1px; }
  .contact .label { font-style: italic; }
  .contact .address { font-size: 17px; }
  .name-band {
    position: absolute; left: 672px; top: 336px;
    width: 378px; height: 88px;
    background: var(--name-band);
    border-radius: 8px 0 0 8px;
    display: flex; align-items: center; padding-left: 30px;
  }
  .person-name {
    font-size: 36px; font-weight: 400; color: #fff; letter-spacing: 0.5px;
  }
</style>
</head>
<body>
  <div class="card">
    <svg class="edge-art edge-art--left" viewBox="0 0 280 600" role="img" aria-label="Teal geometric decoration along the left edge">
      <defs>
        <linearGradient id="leftTone" x1="0" y1="0" x2="1" y2="0">
          <stop offset="0" stop-color="#5cc2a8"/>
          <stop offset="1" stop-color="#22977a"/>
        </linearGradient>
      </defs>
      <polygon points="0,0 40,0 270,600 0,600" fill="url(#leftTone)"/>
    </svg>

    <svg class="edge-art edge-art--right" viewBox="0 0 430 600" role="img" aria-label="Teal geometric decoration along the right edge">
      <defs>
        <linearGradient id="rightTone" x1="0" y1="0" x2="1" y2="1">
          <stop offset="0" stop-color="#32a085"/>
          <stop offset="1" stop-color="#1a5b4a"/>
        </linearGradient>
      </defs>
      <polygon points="202,0 385,105 430,250 430,600 15,600" fill="url(#rightTone)"/>
    </svg>

    <div class="brand">
      <span class="brand-dot"></span>
      <span class="brand-name">Brightwave Renewables</span>
    </div>

    <ul class="contact">
      <li>
        <svg viewBox="0 0 24 24"><path d="M3 9c0-3 4-5 9-5s9 2 9 5v2h-5V9c-1-.6-2.4-1-4-1s-3 .4-4 1v2H3zM6 12h12l2 8H4zm6 1.5a3 3 0 100 6 3 3 0 000-6z"/></svg>
        <span><span class="label">Direct:</span> +1 (555) 014-2276</span>
      </li>
      <li>
        <svg viewBox="0 0 24 24"><path d="M2 5h20v14H2zm2 2v.5l8 6 8-6V7zm0 3v7h16v-7l-8 6z"/></svg>
        <span>daniel.corvane@brightwave-renewables.com</span>
      </li>
      <li>
        <svg viewBox="0 0 24 24"><path d="M12 1a8 8 0 00-8 8c0 6 8 14 8 14s8-8 8-14a8 8 0 00-8-8zm0 5a3 3 0 110 6 3 3 0 010-6z"/></svg>
        <span class="address">Brightwave Renewables LLC<br>218 Harbor Street, Portland, ME 04101</span>
      </li>
    </ul>

    <div class="name-band">
      <span class="person-name">DANIEL CORVANE</span>
    </div>
  </div>
</body>
</html>
```